Dravlin equipment and Dravlin Morenzo

Looking for to get new business cards with two different companies on it. It can be either one company on one side and the company on the other side. Both address are the same. Would like to use the blue and orange in the logo for the theme

Target Market(s)

Construction equipment

Contact Information for Business Card

4817 s Pelham crane blvd
Irving tx 75093

Phone:972-418-6605

Website need to be on

Employee name, mobile and address

Colors

Designer to choose colors to be used in the design.

Requirements
Must have
• Bold logo, have to incorporate both logos on the card

```html
<!DOCTYPE html>
<html lang="en">
<head>
<meta charset="utf-8">
<title>Dravlin business cards</title>
<link rel="stylesheet" href="https://fonts.googleapis.com/css2?family=Roboto:wght@400;500;700;900&display=swap">
<style>
  :root {
    --bg: #e6e6e6;
    --paper: #ffffff;
    --blue: #1762b8;
    --blue-dark: #0f3f7a;
    --ink: #3d3d3d;
    --rule: #9a9a9a;
    --orange: #ec5a2a;
    --orange-light: #f3774a;
    --orange-deep: #d9481c;
  }
  html, body {
    margin: 0;
    width: 1200px;
    height: 800px;
    overflow: hidden;
    background: var(--bg);
    font-family: "Roboto", Arial, sans-serif;
  }
  .stage {
    position: relative;
    width: 1200px;
    height: 800px;
  }
  .card {
    position: absolute;
    top: 245px;
    width: 540px;
    height: 310px;
    box-shadow: 0 6px 18px rgba(0,0,0,0.18);
    box-sizing: border-box;
  }
  /* Front: contact side */
  .card--front {
    left: 40px;
    background: var(--paper);
    border-bottom: 4px solid var(--blue);
    border-left: 4px solid var(--blue);
    display: flex;
    align-items: center;
  }
  .brand {
    width: 250px;
    display: flex;
    align-items: center;
    justify-content: center;
    gap: 10px;
  }
  .brand__mark {
    width: 22px;
    height: 22px;
    background: var(--blue);
  }
  .brand__name {
    font-size: 22px;
    font-weight: 900;
    color: var(--blue-dark);
    letter-spacing: 0.5px;
  }
  .divider {
    width: 1px;
    height: 190px;
    background: var(--rule);
  }
  .contact {
    padding-left: 28px;
    color: var(--ink);
    font-size: 14px;
    line-height: 1.4;
  }
  .contact__name {
    margin: 0;
    font-size: 19px;
    font-weight: 500;
    color: var(--blue);
    letter-spacing: 0.5px;
  }
  .contact__title {
    margin: 0 0 12px;
    font-size: 15px;
  }
  .contact__address {
    margin: 0 0 10px;
    font-style: normal;
  }
  .contact__list {
    list-style: none;
    margin: 0;
    padding: 0;
  }
  .contact__list li {
    display: flex;
    align-items: center;
    gap: 8px;
  }
  .contact__list svg {
    width: 12px;
    height: 12px;
    fill: none;
    stroke: var(--blue);
    stroke-width: 2;
  }
  .contact__web span { color: var(--blue); }

  /* Back: orange brand side */
  .card--back {
    left: 620px;
    overflow: hidden;
    display: flex;
    align-items: center;
    justify-content: center;
  }
  .card__pattern {
    position: absolute;
    inset: 0;
    background: radial-gradient(circle at 75% 60%, var(--orange-light), var(--orange) 55%, var(--orange-deep));
  }
  .brand--back {
    position: relative;
    width: auto;
    gap: 14px;
  }
  .brand--back .brand__mark {
    width: 30px;
    height: 30px;
    background: var(--paper);
  }
  .brand--back .brand__name {
    color: var(--paper);
    font-size: 30px;
  }
</style>
</head>
<body>
<main class="stage">
  <section class="card card--front">
    <div class="brand">
      <span class="brand__mark"></span>
      <span class="brand__name">Dravlin equipment</span>
    </div>
    <div class="divider"></div>
    <div class="contact">
      <h1 class="contact__name">MARCUS HALE</h1>
      <p class="contact__title">Manager</p>
      <address class="contact__address">4817 s Pelham crane blvd<br>Irving tx 75093</address>
      <ul class="contact__list">
        <li>
          <svg viewBox="0 0 12 12"><path d="M2 1 L4 1 L5 4 L3.5 5 A6 6 0 0 0 7 8.5 L8 7 L11 8 L11 10 A1 1 0 0 1 10 11 A9 9 0 0 1 1 2 A1 1 0 0 1 2 1 Z"/></svg>
          972-418-6605
        </li>
        <li>
          <svg viewBox="0 0 12 12"><rect x="1" y="2.5" width="10" height="7"/><path d="M1 2.5 L6 6.5 L11 2.5"/></svg>
          mhale@dravlinequip.com
        </li>
        <li class="contact__web">
          <svg viewBox="0 0 12 12"><circle cx="6" cy="6" r="5"/><path d="M1 6 H11 M6 1 C3 4 3 8 6 11 M6 1 C9 4 9 8 6 11"/></svg>
          www.<span>dravlinequip</span>.com
        </li>
      </ul>
    </div>
  </section>

  <section class="card card--back">
    <div class="card__pattern" role="img" aria-label="Embossed repeating hexagon brand pattern in orange tones"></div>
    <div class="brand brand--back">
      <span class="brand__mark"></span>
      <span class="brand__name">Dravlin Morenzo</span>
    </div>
  </section>
</main>
</body>
</html>
```